The Balanced Plate Hour with Dan Orrick.

I'm launching this podcast on health and wellness and I want to be take serious. That starts with a great design. There's too much contradiction out there about what is and isn't healthy. I want my podcast to be a resource that people can rely upon. I want my face in it and I want it to pop with colors that catch the eye. I want It clean and crisp. I was also thinking of experimenting with an animated photo of me as well. What ever looks best.

Industry/Entity Type

Health And Wellness

Font styles to use
Sans Serif

Requirements
Must have
• My face and or body.

```html
<!DOCTYPE html>
<html lang="en">
<head>
<meta charset="utf-8">
<title>The Balanced Plate Hour with Dan Orrick</title>
<link rel="stylesheet" href="https://fonts.googleapis.com/css2?family=Alfa+Slab+One&family=Anton&family=Oswald:wght@500&family=Questrial&display=swap">
<style>
  :root {
    --page: #2b1d17;
    --red-deep: #8f1a1c;
    --red: #d8342c;
    --coral: #f0664f;
    --blush: #fbd3c6;
    --cream: #f6d6c4;
    --white: #ffffff;
    --black: #050505;
  }
  html, body {
    margin: 0;
    width: 1200px;
    height: 1200px;
    overflow: hidden;
    background: var(--page);
  }
  .show-card {
    position: absolute;
    left: 50px;
    top: 173px;
    width: 1100px;
    height: 853px;
    box-shadow: 0 20px 40px rgba(0,0,0,.45);
  }
  .show-card svg { display: block; }
  .kicker { font-family: "Oswald", sans-serif; font-weight: 500; font-size: 46px; fill: var(--cream); }
  .headline { font-family: "Alfa Slab One", serif; font-size: 104px; fill: var(--white); }
  .subline { font-family: "Questrial", sans-serif; font-size: 68px; fill: var(--white); }
  .host-name { font-family: "Anton", sans-serif; font-size: 104px; fill: var(--black); stroke: var(--white); stroke-width: 2; paint-order: stroke; }
  .text-shadow { filter: drop-shadow(3px 4px 3px rgba(0,0,0,.55)); }
</style>
</head>
<body>
<div class="show-card">
  <svg width="1100" height="853" viewBox="0 0 1100 853" xmlns="http://www.w3.org/2000/svg">
    <defs>
      <radialGradient id="glow" cx="78%" cy="40%" r="75%">
        <stop offset="0" stop-color="#fff1ea"/>
        <stop offset="0.35" stop-color="var(--coral)"/>
        <stop offset="0.75" stop-color="var(--red)"/>
        <stop offset="1" stop-color="var(--red-deep)"/>
      </radialGradient>
      <linearGradient id="portrait-tone" x1="0" y1="0" x2="1" y2="1">
        <stop offset="0" stop-color="#b0605a" stop-opacity=".8"/>
        <stop offset="1" stop-color="#6e1416" stop-opacity=".85"/>
      </linearGradient>
      <linearGradient id="figure-tone" x1="0" y1="0" x2="0" y2="1">
        <stop offset="0" stop-color="#c98a6c"/>
        <stop offset="1" stop-color="#9c5a42"/>
      </linearGradient>
    </defs>

    <rect class="backdrop" width="1100" height="853" fill="url(#glow)"/>
    <g class="facets" fill="var(--white)">
      <polygon points="0,90 1100,0 1100,40 0,120" opacity=".12"/>
      <polygon points="200,0 700,560 620,560 120,0" opacity=".18"/>
      <polygon points="900,0 1100,260 1100,330 860,0" opacity=".2"/>
      <polygon points="1020,0 1100,0 1100,120" opacity=".25"/>
      <polygon points="960,500 1100,420 1100,480" opacity=".2"/>
    </g>

    <rect class="portrait-backdrop" role="img" aria-label="Faded close-up portrait of the host" x="0" y="0" width="440" height="750" fill="url(#portrait-tone)"/>
    <rect class="host-figure" role="img" aria-label="Full-length photo of the host standing shirtless" x="655" y="150" width="345" height="600" rx="6" fill="url(#figure-tone)"/>

    <polygon class="band-red" points="0,688 1100,805 1100,853 0,853" fill="var(--red-deep)"/>
    <polygon class="band-wedge" points="660,760 1100,652 1100,770 800,790" fill="var(--black)"/>
    <polygon class="band-black" points="0,772 1100,812 1100,853 0,853" fill="var(--black)"/>

    <g class="title text-shadow">
      <text class="kicker" x="104" y="402">The Balanced</text>
      <text class="headline" x="104" y="495">Plate</text>
      <text class="subline" x="104" y="577">Hour with</text>
      <text class="host-name" x="263" y="705" transform="rotate(-4 263 705)">Dan Orrick</text>
      <polygon class="name-stripe" points="288,719 674,681 674,712 300,723" fill="var(--white)"/>
    </g>
  </svg>
</div>
</body>
</html>
```